Electronic Time-sheet for phones

I need a time-sheet that can be accessed on the phone, be completed, then have the ability to electronically sign. The time sheet needs to be used two fold for supervision to verify hours and quantities and also for the client to be able to electronically sign. The time-sheet should be daily or weekly if we can get the data to fit. We are trying to streamline field supervisors having to log on to a computer to access a server just to do time-sheets. We need it to be user friendly. We need to have two places to have electronic signatures. One for supervisor or authorized representative and the other for the client to sign.

Target Market(s)

Industrial clients

Industry/Entity Type

Oil And Gas

Requirements
Must have
• hours, quantities, project name, location, signature line etc
Nice to have
• n/a
Should not have
• n/a

```html
<!DOCTYPE html>
<html lang="en">
<head>
<meta charset="utf-8">
<title>Formans Daily Time Sheets</title>
<link href="https://fonts.googleapis.com/css2?family=Montserrat:ital,wght@0,500;0,600;0,700;1,500&display=swap" rel="stylesheet">
<style>
  :root {
    --brand: #2f5cff;
    --page: #e9eefd;
    --card: #f4f6fe;
    --white: #ffffff;
    --text: #555a66;
    --muted: #9aa3bd;
    --field: #f6f7fa;
    --photo-a: #8d8f99;
    --photo-b: #5b5e69;
  }
  * { box-sizing: border-box; margin: 0; padding: 0; }
  html, body { width: 675px; height: 1200px; overflow: hidden; }
  body {
    position: relative;
    background: var(--page);
    font-family: "Montserrat", sans-serif;
  }
  .app-header {
    position: absolute; left: 0; top: 0; width: 675px; height: 162px;
    background: var(--brand); color: var(--white);
  }
  .status-bar {
    position: absolute; left: 0; top: 0; width: 100%; height: 64px;
    display: flex; align-items: center; justify-content: space-between;
    padding: 0 40px 0 58px; font-weight: 600; font-size: 25px;
  }
  .status-icons { display: flex; gap: 10px; align-items: center; }
  .screen-title {
    position: absolute; left: 0; right: 0; top: 102px;
    text-align: center; font-weight: 700; font-size: 29px; letter-spacing: 0.2px;
  }
  .staff-list { position: absolute; left: 0; top: 162px; width: 675px; height: 1038px; }
  .staff-row {
    position: absolute; left: 31px; width: 610px; height: 178px;
  }
  .staff-card {
    position: absolute; left: 0; top: 0; width: 610px; height: 122px;
    background: var(--card); border-radius: 6px;
  }
  .staff-photo {
    position: absolute; left: 0; top: 0; width: 122px; height: 122px;
    border-radius: 8px;
    background: radial-gradient(circle at 50% 40%, var(--photo-a), var(--photo-b));
  }
  .staff-name {
    position: absolute; left: 163px; top: 26px;
    display: flex; align-items: center; gap: 18px;
    color: var(--brand); font-weight: 700; font-size: 25px;
  }
  .staff-meta {
    position: absolute; left: 194px; top: 78px;
    color: var(--muted); font-style: italic; font-weight: 500; font-size: 20px;
    word-spacing: 2px;
  }
  .staff-meta span + span { margin-left: 22px; }
  .more-tag {
    position: absolute; left: 482px; top: 124px; width: 128px; height: 50px;
  }
  .more-tag span {
    position: absolute; inset: 0; display: flex; align-items: center; justify-content: center;
    padding-left: 18px; color: var(--white); font-size: 16px; font-weight: 600;
  }
  .list-veil {
    position: absolute; left: 0; top: 162px; width: 675px; height: 1038px;
    background: rgba(240, 244, 255, 0.78);
  }
  .filter-panel {
    position: absolute; left: 205px; top: 162px; width: 436px; height: 212px;
    background: var(--white); border-radius: 8px;
    box-shadow: 0 8px 22px rgba(40, 60, 120, 0.22);
    padding-top: 30px;
  }
  .filter-field {
    display: flex; align-items: center; height: 38px; margin-bottom: 24px;
  }
  .filter-field label {
    width: 171px; text-align: right; padding-right: 11px;
    color: var(--text); font-weight: 600; font-size: 20px;
  }
  .filter-field .field-input {
    width: 221px; height: 38px; background: var(--field); border-radius: 5px;
  }
  .close-button {
    position: absolute; left: 574px; top: 104px; width: 67px; height: 67px;
    background: var(--white); border-radius: 8px;
    display: flex; align-items: center; justify-content: center;
  }
</style>
</head>
<body>
  <header class="app-header">
    <div class="status-bar">
      <span>9:41</span>
      <span class="status-icons">
        <svg width="30" height="20" viewBox="0 0 30 20"><rect x="0" y="13" width="5" height="7" rx="1" fill="#fff"/><rect x="8" y="9" width="5" height="11" rx="1" fill="#fff"/><rect x="16" y="5" width="5" height="15" rx="1" fill="#fff"/><rect x="24" y="0" width="5" height="20" rx="1" fill="#fff"/></svg>
        <svg width="28" height="20" viewBox="0 0 28 20"><path d="M2 7a17 17 0 0 1 24 0M6 11a11 11 0 0 1 16 0M10 15a5 5 0 0 1 8 0" stroke="#fff" stroke-width="3" fill="none" stroke-linecap="round"/><circle cx="14" cy="18" r="2" fill="#fff"/></svg>
        <svg width="42" height="20" viewBox="0 0 42 20"><rect x="1" y="1" width="36" height="18" rx="5" stroke="#fff" stroke-width="2" fill="none"/><rect x="4" y="4" width="30" height="12" rx="3" fill="#fff"/><rect x="39" y="7" width="3" height="6" rx="1" fill="#fff"/></svg>
      </span>
    </div>
    <h1 class="screen-title">Formans Daily Time Sheets</h1>
  </header>

  <main class="staff-list">
    <article class="staff-row" style="top:29px">
      <div class="staff-card"></div>
      <div class="staff-photo" role="img" aria-label="Employee portrait photo"></div>
      <div class="staff-name"><svg width="30" height="30" viewBox="0 0 24 24"><circle cx="12" cy="7" r="5" fill="#2f5cff"/><path d="M2 23c0-6 4.5-9 10-9s10 3 10 9z" fill="#2f5cff"/></svg>John Doe</div>
    </article>
    <article class="staff-row" style="top:218px">
      <div class="staff-card"></div>
      <div class="staff-photo" role="img" aria-label="Employee portrait photo"></div>
      <div class="staff-name"><svg width="30" height="30" viewBox="0 0 24 24"><circle cx="12" cy="7" r="5" fill="#2f5cff"/><path d="M2 23c0-6 4.5-9 10-9s10 3 10 9z" fill="#2f5cff"/></svg>John Doe</div>
      <div class="staff-meta"><span>Class: JE-A</span><span>Emp-No: 1547</span></div>
      <div class="more-tag"><svg width="128" height="50" viewBox="0 0 128 50"><path d="M0 0H128V50H30z" fill="#2f5cff"/></svg><span>MORE</span></div>
    </article>
    <article class="staff-row" style="top:409px">
      <div class="staff-card"></div>
      <div class="staff-photo" role="img" aria-label="Employee portrait photo"></div>
      <div class="staff-name"><svg width="30" height="30" viewBox="0 0 24 24"><circle cx="12" cy="7" r="5" fill="#2f5cff"/><path d="M2 23c0-6 4.5-9 10-9s10 3 10 9z" fill="#2f5cff"/></svg>John Doe</div>
      <div class="staff-meta"><span>Class: JE-A</span><span>Emp-No: 1547</span></div>
      <div class="more-tag"><svg width="128" height="50" viewBox="0 0 128 50"><path d="M0 0H128V50H30z" fill="#2f5cff"/></svg><span>MORE</span></div>
    </article>
    <article class="staff-row" style="top:599px">
      <div class="staff-card"></div>
      <div class="staff-photo" role="img" aria-label="Employee portrait photo"></div>
      <div class="staff-name"><svg width="30" height="30" viewBox="0 0 24 24"><circle cx="12" cy="7" r="5" fill="#2f5cff"/><path d="M2 23c0-6 4.5-9 10-9s10 3 10 9z" fill="#2f5cff"/></svg>John Doe</div>
      <div class="staff-meta"><span>Class: JE-A</span><span>Emp-No: 1547</span></div>
      <div class="more-tag"><svg width="128" height="50" viewBox="0 0 128 50"><path d="M0 0H128V50H30z" fill="#2f5cff"/></svg><span>MORE</span></div>
    </article>
    <article class="staff-row" style="top:790px">
      <div class="staff-card"></div>
      <div class="staff-photo" role="img" aria-label="Employee portrait photo"></div>
      <div class="staff-name"><svg width="30" height="30" viewBox="0 0 24 24"><circle cx="12" cy="7" r="5" fill="#2f5cff"/><path d="M2 23c0-6 4.5-9 10-9s10 3 10 9z" fill="#2f5cff"/></svg>John Doe</div>
      <div class="staff-meta"><span>Class: JE-A</span><span>Emp-No: 1547</span></div>
      <div class="more-tag"><svg width="128" height="50" viewBox="0 0 128 50"><path d="M0 0H128V50H30z" fill="#2f5cff"/></svg><span>MORE</span></div>
    </article>
    <article class="staff-row" style="top:981px">
      <div class="staff-card"></div>
      <div class="staff-photo" role="img" aria-label="Employee portrait photo"></div>
      <div class="staff-name"><svg width="30" height="30" viewBox="0 0 24 24"><circle cx="12" cy="7" r="5" fill="#2f5cff"/><path d="M2 23c0-6 4.5-9 10-9s10 3 10 9z" fill="#2f5cff"/></svg>John Doe</div>
    </article>
  </main>

  <div class="list-veil"></div>

  <section class="filter-panel">
    <div class="filter-field"><label>Forman :</label><div class="field-input"></div></div>
    <div class="filter-field"><label>Approved By :</label><div class="field-input"></div></div>
    <div class="filter-field"><label>Date :</label><div class="field-input"></div></div>
  </section>

  <div class="close-button" aria-label="Close">
    <svg width="32" height="32" viewBox="0 0 32 32"><path d="M4 4L28 28M28 4L4 28" stroke="#2f5cff" stroke-width="4" stroke-linecap="round"/></svg>
  </div>
</body>
</html>
```